2 Wine Label Designs

Amberly Cellars has been helping people give customized wine gifts since 1999. From large scale corporate clients, to 1 bottle personalized gifts, we offer a wide range of wines and templates for any occasion. Recently we’ve started to shift our focus to a younger demographic (21 to 35 year old women) and are in the process of updating our website and branding.

One big area we’re working to improve is the customizable wine label/engraving templates we offer on the site (to see our current template library go to www.amberlycellars.com/shop/wine, select a wine, choose “label” or “engraving” from the dropdown, and click “customize”). You’ll find that a lot of our current templates are outdated or aimed at an older demographic. Over the next few months we want to swap out most of these old templates with fun fresh designs.

We're asking designers to submit 2 customizable wine label templates for this project. One should be wedding themed and the other "Thank You" themed. Please see the attached PDF for more guidelines and creative direction.

Keep in mind, even if you aren't selected as the winner of this project we are going to go through and offer $50 for any label template submitted that we like ($100 if we want both). So there is a good chance you'll be getting some money for your work!

Please read though the attached guidelines PDF carefully (especially the "Must be Customizable" section).

Target Market(s)

21 to 35 year old women

Colors

Designer to choose colors to be used in the design.

Requirements
Must have
• See attached PDF
Nice to have
• See attached PDF
Should not have
• See attached PDF

```html
<!DOCTYPE html>
<html lang="en">
<head>
<meta charset="utf-8">
<title>Happily Ever After – Wedding Wine Label</title>
<link href="https://fonts.googleapis.com/css2?family=Playball&display=swap" rel="stylesheet">
<style>
  :root {
    --canvas-bg: #e9e7e8;
    --label-bg: #f8f4f6;
    --label-edge: #e4dde2;
    --ink-gold: #a3713f;
    --rule-dark: #3b3a3c;
    --ornament-light: #efe9d6;
    --ornament-mid: #d6cca4;
  }
  * { margin: 0; padding: 0; box-sizing: border-box; }
  html, body {
    width: 1200px;
    height: 900px;
    overflow: hidden;
    background: var(--canvas-bg);
  }
  .canvas {
    position: relative;
    width: 1200px;
    height: 900px;
    display: flex;
    align-items: center;
    justify-content: center;
  }
  .wine-label {
    position: relative;
    width: 420px;
    height: 840px;
    background: var(--label-bg);
    border: 1px solid var(--label-edge);
  }
  .ornament {
    position: absolute;
    left: 40px;
    width: 340px;
    height: 140px;
    border-radius: 70px;
    background: radial-gradient(ellipse at center, var(--ornament-mid) 0%, var(--ornament-light) 55%, var(--label-bg) 80%);
  }
  .ornament--top { top: 20px; }
  .ornament--bottom { top: 690px; }
  .rule {
    position: absolute;
    height: 0;
    border-top: 1.5px solid var(--rule-dark);
  }
  .rule--a { top: 192px; left: 46px; width: 358px; }
  .rule--b { top: 222px; left: 30px; width: 370px; }
  .rule--c { top: 640px; left: 30px; width: 370px; border-top-style: dashed; }
  .rule--d { top: 672px; left: 46px; width: 358px; border-top-style: dashed; }
  .label-title {
    position: absolute;
    top: 250px;
    left: 0;
    width: 100%;
    text-align: center;
    font-family: "Playball", cursive;
    color: var(--ink-gold);
    line-height: 1;
  }
  .label-title span { display: block; }
  .label-title .line-1 { font-size: 104px; margin-bottom: 38px; }
  .label-title .line-2 { font-size: 78px; margin-bottom: 60px; }
  .label-title .line-3 { font-size: 82px; }
</style>
</head>
<body>
  <main class="canvas">
    <section class="wine-label">
      <div class="ornament ornament--top" role="img" aria-label="Pair of mirrored gold and sage leaf scroll flourishes"></div>
      <div class="rule rule--a"></div>
      <div class="rule rule--b"></div>
      <h1 class="label-title">
        <span class="line-1">Happily</span>
        <span class="line-2">ever</span>
        <span class="line-3">after</span>
      </h1>
      <div class="rule rule--c"></div>
      <div class="rule rule--d"></div>
      <div class="ornament ornament--bottom" role="img" aria-label="Pair of mirrored gold and sage leaf scroll flourishes"></div>
    </section>
  </main>
</body>
</html>
```